VitalHaven.Studio - Trifold Brochure

Requirements: Phase 1 - Trifold brochure (in the spirit of existing brand look and feel). [Phase - subject to the success of Phase 1 - leaflet design with services, business card design - not to be quoted in this task] . Phase 3 - One page website

Yet to be launched concept VitalHaven.Studio (will launch in 2 days), has been established initially to serve a very specific audience - women, 30s-40s, with seeking higher levels fo wellness. Already settled with the alternative health modalities, but desperate for more energy, needing direction on their path, and potentially support and care in the form of coaching and mentoring.

The clinic is launching with a unique offer, using technology to assess for areas of their life, mind and body that need attention. The technology is being offered for Free, Lifetime, Unlimited Access to those who buy a small piece of hardware that is able to "read" how their body is working. It can be used by more than one person (useful for families)

The technology is not owned by the clinic, only licensed by. The clinic facilitates the onboarding of the client to the platform and teaches the how to read it, and navigate the instructions contained within to improve energy. .There are other services available from the clinic which are higher touch - 30 and 90 day protocols including, health strategy, accountability, which drive deeper transformation.

Some design work has been done .
I need a designer to carry on from the prior designer, on a tight deadline for this Phase.

We have logo, brand colours and double sided leaflet that will help understand the look and feel of the brand.

This Phase is about Trifold DL. Despite all services being delivered online, the launch and this project relates to the launch which will be run out of an offline clinic (joint venture partner) . This brochure will be handed to the client on completing their initial scan (for free) and given their access to their online account.

This brochure should show case the clinic, a few testimonials,
the practitioner behind the clinic, call to action is move along the path step by step...will outline.

I need a designer to take the existing brand concept, and help me build the trifold brochure with a 48 hour deadline, so that we may move to Phase 2 & 3 of the launch project. I want to just focus on the trifold at this stage.

Need extra days to review

Here is the link to the Brightgrid Sheet again https://files.examplecloud.net/sheets/d/7qTr-Kc2LMNpawXz84RdBuvE93hoxYtVQ1JmKP5Sg2nu/view?usp=sharing

Target Market(s)

Women aged 30-50

Industry/Entity Type

Health And Wellness

Colors
88d0c7
33a6d7
3176b5

Requirements
Must have
• Draw from colour palette provided - se two page brochure as a guideline
Broad lay out per the powerpoint provided
Should not have
• no pictures of men

```html
<!DOCTYPE html>
<html lang="en">
<head>
<meta charset="utf-8">
<title>VitalHaven.Studio – Trifold Brochure</title>
<link href="https://fonts.googleapis.com/css2?family=Montserrat:wght@400;500;600;700&display=swap" rel="stylesheet">
<style>
:root{
  --teal:#88d0c7;
  --aqua:#2bb3b6;
  --sky:#33a6d7;
  --navy:#3176b5;
  --ink:#2c2f38;
  --paper:#ffffff;
  --stage:#ececec;
  --rule:#9aa3ad;
}
*{box-sizing:border-box;margin:0;padding:0}
html,body{width:1200px;height:2297px;overflow:hidden;background:var(--stage)}
body{font-family:"Montserrat",sans-serif;color:var(--ink);position:relative}
.spread{position:absolute;left:40px;width:1120px;height:794px;background:var(--paper);overflow:hidden;box-shadow:0 2px 10px rgba(0,0,0,.12)}
.spread--outside{top:310px}
.spread--inside{top:1190px}
.abs{position:absolute}
.backdrop{position:absolute;left:0;top:0}

.brand{display:flex;align-items:center;gap:8px;color:var(--aqua);font-weight:600;white-space:nowrap}
.brand__dot{width:22px;height:22px;border-radius:50%;background:var(--teal)}

/* outside – panel 1 */
.offer{left:39px;top:212px;width:320px}
.offer__kicker{color:var(--aqua);font-size:14px;letter-spacing:.3px;text-transform:uppercase}
.offer__title{font-weight:700;font-size:14px;line-height:1.25;text-transform:uppercase;letter-spacing:.3px}
.pillars{left:39px;top:276px;width:320px;font-size:10.5px;line-height:1.35}
.pillars p{margin-bottom:8px}
.pillars b{color:var(--sky);font-weight:700}
.start{left:39px;top:484px;width:320px;color:#fff}
.start__title{font-size:19px;line-height:1.05;font-weight:500;letter-spacing:.5px}
.start__title b{display:block;color:var(--teal);font-weight:700}
.steps{list-style:none;margin-top:18px;font-size:10.5px;font-weight:600}
.steps li{display:flex;align-items:flex-start;gap:14px;margin-bottom:11px}
.steps .num{flex:none;width:16px;height:16px;border-radius:50%;background:#fff;color:var(--navy);font-size:9px;font-weight:700;display:flex;align-items:center;justify-content:center;box-shadow:0 0 0 2px rgba(136,208,199,.6)}
.steps .sub{display:flex;gap:16px;font-weight:500;font-size:9px;margin:-5px 0 9px 30px}
.steps .sub span::before{content:"";display:inline-block;width:6px;height:6px;border-radius:50%;background:var(--teal);margin-right:6px}

/* outside – panel 2 */
.pill{left:448px;top:46px;width:222px;height:40px;border-radius:20px;background:#e6e9ee;color:var(--navy);font-weight:700;font-size:22px;letter-spacing:1px;display:flex;align-items:center;justify-content:center;box-shadow:0 2px 3px rgba(0,0,0,.12)}
.quote{left:424px;width:268px;border:1.5px solid #d5dae0;border-radius:10px;padding:14px 14px 10px;font-size:10.5px;line-height:1.3;text-align:justify;background:#fff}
.quote::before,.quote::after{position:absolute;color:var(--teal);font-size:30px;font-weight:700;line-height:1;font-family:Georgia,serif}
.quote::before{content:"\201C";left:2px;top:-24px}
.quote::after{content:"\201D";right:12px;bottom:-22px}
.quote cite{display:block;text-align:right;color:var(--sky);font-style:normal;font-weight:600;font-size:10px;margin-top:4px}
.q1{top:130px}.q2{top:240px}.q3{top:378px}
.contact{left:412px;top:604px;width:300px;color:#fff;font-size:11px}
.contact h3{font-weight:500;font-size:17px;letter-spacing:.5px;margin-bottom:12px}
.contact .lead{margin-bottom:12px}
.contact ul{list-style:none}
.contact li{display:flex;gap:10px;margin-bottom:6px;align-items:flex-start}
.contact svg{flex:none;margin-top:2px}
.contact .phone{color:var(--teal);font-weight:700}
.contact-brand{left:600px;top:742px;font-size:12px;color:#fff}
.contact-brand .brand__dot{width:14px;height:14px;background:#fff}

/* outside – panel 3 */
.cover-brand{left:820px;top:78px;font-size:22px}
.cover-brand .brand__dot{width:34px;height:34px}
.cover-title{left:784px;top:640px;color:#fff;font-size:34px;line-height:1;font-weight:400;letter-spacing:.5px}
.cover-title b{display:block;color:var(--teal);font-weight:700;font-size:30px;margin-top:2px}
.cover-lead{left:784px;top:718px;width:300px;color:#e3eef8;font-size:9.5px;line-height:1.3}
.cover-web{left:784px;top:754px;color:#fff;font-weight:700;font-size:11px}

/* inside – table */
.screens{left:37px;top:32px;width:660px;border-collapse:collapse;font-size:7.4px;line-height:1.28;table-layout:fixed}
.screens th{background:var(--aqua);color:#fff;font-weight:600;font-size:10px;text-align:left;height:30px;padding:0 8px;letter-spacing:.4px}
.screens th:first-child{border-top-left-radius:10px}
.screens th:last-child{border-top-right-radius:10px;font-size:8px;line-height:1.05}
.screens td{border:1px solid var(--rule);height:61.6px;padding:3px 6px;vertical-align:middle}
.screens td.name{font-size:7.8px}
.screens td.howto{vertical-align:top;padding-top:12px}
.screens tr:first-child td{border-top:none}
.inside-brand{left:37px;top:744px;font-size:16px}
.bottles{left:240px;top:700px;width:470px;height:76px;border-radius:4px;background:linear-gradient(180deg,#6b3d1f 0%,#a0612e 45%,#e8ecef 46%,#f6f7f8 100%)}

/* inside – practitioner panel */
.bio-panel{left:736px;top:0;width:384px;height:794px;background:linear-gradient(180deg,var(--navy) 0%,var(--sky) 100%)}
.portrait{left:770px;top:48px;width:100px;height:100px;border-radius:50%;border:3px solid #fff;box-shadow:0 0 0 2px var(--teal);background:radial-gradient(circle at 50% 40%,#c6cbd1,#7f8a95)}
.bio-name{left:918px;top:64px;color:#fff;font-size:19px;font-weight:600}
.bio-creds{left:918px;top:92px;color:#dde9f4;font-size:9.5px;letter-spacing:.4px}
.bio{left:771px;top:176px;width:318px;color:#fff;font-size:9.5px;line-height:1.28;text-align:justify}
.bio p{margin-bottom:10px}
.bio-quote{left:771px;top:518px;width:318px;border:1px solid rgba(255,255,255,.6);padding:10px 14px 8px;color:#fff;font-size:9.5px;line-height:1.3}
.bio-quote::before,.bio-quote::after{position:absolute;color:var(--teal);font-size:26px;font-weight:700;font-family:Georgia,serif;line-height:1}
.bio-quote::before{content:"\201C";left:-2px;top:-20px}
.bio-quote::after{content:"\201D";right:-4px;bottom:-18px}
.bio-quote cite{display:block;text-align:right;font-style:normal;font-weight:600;margin-top:4px}
</style>
</head>
<body>

<section class="spread spread--outside" aria-label="Brochure outside spread">
  <svg class="backdrop" width="1120" height="794" viewBox="0 0 1120 794">
    <defs>
      <linearGradient id="ocean" x1="0" y1="0" x2="0" y2="1">
        <stop offset="0" stop-color="#33a6d7"/><stop offset="1" stop-color="#3176b5"/>
      </linearGradient>
      <linearGradient id="skyPhoto" x1="0" y1="0" x2="0" y2="1">
        <stop offset="0" stop-color="#7fb3d8"/><stop offset=".55" stop-color="#c4dcec"/><stop offset="1" stop-color="#eaf2f8"/>
      </linearGradient>
      <linearGradient id="dawnPhoto" x1="0" y1="0" x2="0" y2="1">
        <stop offset="0" stop-color="#9fb4c6"/><stop offset=".6" stop-color="#dfe3e6"/><stop offset="1" stop-color="#5d6b73"/>
      </linearGradient>
    </defs>
    <g role="img" aria-label="Photo: woman holding a blue scarf in the wind against a bright sky">
      <rect x="747" y="0" width="373" height="600" fill="url(#skyPhoto)"/>
    </g>
    <g role="img" aria-label="Photo: woman in a yoga pose above the clouds facing a mountain peak">
      <path d="M0,0 H373 C330,110 200,182 0,196 Z" fill="url(#dawnPhoto)"/>
    </g>
    <path d="M373,0 C330,110 200,182 0,196" fill="none" stroke="#3176b5" stroke-width="5"/>
    <path d="M0,414 C180,390 330,482 560,506 C760,530 900,444 1120,362 L1120,392 C900,474 760,558 560,532 C330,506 180,418 0,444 Z" fill="#2bb3b6"/>
    <path d="M0,444 C180,418 330,506 560,532 C760,558 900,474 1120,392 L1120,794 L0,794 Z" fill="url(#ocean)"/>
  </svg>

  <div class="abs offer">
    <p class="offer__kicker">Lifetime access to the software &amp;</p>
    <p class="offer__title">Education is currently free to qualified applicants</p>
  </div>
  <div class="abs pillars">
    <p><b>DETECT:</b> Uncover the reasons why you feel the way you feel.</p>
    <p><b>DIRECT:</b> Find direction on what to put your energy into</p>
    <p><b>CORRECT:</b> Enjoy the energetic support from Kelvaro Bio-energetics Bio-tonics or the Professional crew at vitalhaven.studio</p>
  </div>

  <div class="abs start">
    <h2 class="start__title">HOW TO GET <b>STARTED</b></h2>
    <ol class="steps">
      <li><span class="num">1</span>Register - vitalhaven.studio/start</li>
      <li><span class="num">2</span>Get Your Scanner - go to shop &amp; buy</li>
      <li><span class="num">3</span>Download App - KelvaSync</li>
      <li><span class="num">4</span>Pair Scanner with your phone</li>
      <li><span class="num">5</span>Scan Away (follow instructions)</li>
      <li><span class="num">6</span>View Results &amp; Information</li>
      <li class="sub"><span>Online or</span><span>On Phone</span></li>
      <li><span class="num">7</span>Follow guidelines within software or make an appointment to have bespoke strategy and protocol designed by Rowan</li>
    </ol>
  </div>

  <div class="abs pill">TESTIMONIALS</div>
  <blockquote class="abs quote q1">Thanks to Kelvaro, my energy has skyrocketed and I am accomplishing more than I have in years<cite>Jenna Carlow</cite></blockquote>
  <blockquote class="abs quote q2">Kelvaro Health truly offers insights into the body, both mind and physical well-being, that the medical community cannot comprehend often, nor understand. It is truly a remarkable system<cite>Dr Helen Marsh</cite></blockquote>
  <blockquote class="abs quote q3">provides the signal for the body to heal itself. What's hard to understand is it really doesn't do anything except provide the signal. The body does everything else<cite>Dr. Owen Pratt, MD</cite></blockquote>

  <div class="abs contact">
    <h3>CONTACT US</h3>
    <p class="lead">E Providing Convenient Remote<br>Service Only</p>
    <ul>
      <li><svg width="10" height="12" viewBox="0 0 10 12"><path d="M5 0a4 4 0 0 1 4 4c0 3-4 8-4 8S1 7 1 4a4 4 0 0 1 4-4z" fill="#88d0c7"/><circle cx="5" cy="4" r="1.5" fill="#3176b5"/></svg><span>Level 8, 42 Harbour Lane,<br>Sydney, Australia</span></li>
      <li><svg width="10" height="10" viewBox="0 0 10 10"><path d="M2 0l2 2.5-1 1.5c.6 1.3 1.6 2.3 3 3l1.5-1L10 8 8.5 10C4 9.5.5 6 0 1.5z" fill="#88d0c7"/></svg><span class="phone">02 9000 4417</span></li>
      <li><svg width="11" height="9" viewBox="0 0 11 9"><rect width="11" height="9" rx="1" fill="#88d0c7"/><path d="M0.5 1l5 4 5-4" fill="none" stroke="#3176b5" stroke-width="1"/></svg><span>rowan@rowanhale.example</span></li>
      <li><svg width="10" height="10" viewBox="0 0 10 10"><circle cx="5" cy="5" r="4.5" fill="#88d0c7"/><path d="M0.5 5h9M5 .5c-2.5 3-2.5 6 0 9M5 .5c2.5 3 2.5 6 0 9" fill="none" stroke="#3176b5" stroke-width=".7"/></svg><span>www.vitalhaven.studio</span></li>
    </ul>
  </div>
  <div class="abs brand contact-brand"><span class="brand__dot"></span>VitalHaven.Studio</div>

  <div class="abs brand cover-brand"><span class="brand__dot"></span>VitalHaven.Studio</div>
  <h1 class="abs cover-title">RESTORE YOUR<b>ENERGY</b></h1>
  <p class="abs cover-lead">Led by Bioenergetic &amp; Functional Diagnostic Nutrition Practitioner</p>
  <p class="abs cover-web">www.vitalhaven.studio</p>
</section>

<section class="spread spread--inside" aria-label="Brochure inside spread">
  <table class="abs screens">
    <colgroup><col style="width:69px"><col style="width:97px"><col style="width:116px"><col style="width:253px"><col style="width:125px"></colgroup>
    <thead><tr><th></th><th>KELVARO SCREEN</th><th>QUESTION</th><th>DESCRIPTION</th><th>HOW TO READ<br>THE SCAN</th></tr></thead>
    <tbody>
      <tr><td></td><td class="name">Energy Source</td><td>How well are you sourcing beneficial energy?</td><td>Energy sources from the environment can power up your body like a battery for a supercharged state of health that can transform your life. With these tools, you can double or even triple your energy. With enough energy, the possibilities become limitless. Eg Your diet, hydration, light, sleep, movement?</td><td class="howto" rowspan="2">1. Look for PURPLE DOTS first (5), and then the information on the right to understand what it is telling you. Look for ORANGE dots second (4).</td></tr>
      <tr><td></td><td class="name">Core Drivers</td><td>How strong are your emotional &amp; creative energies, and how well is energy being driven?</td><td>The energy of each organ or system has a particular energetic pattern and "feel" to it. We can look at the strength of our emotional and creative energies in relation to these Driver fields. There are 16 Core Drivers. Eg Heart, Liver, Spleen, Circulation</td></tr>
      <tr><td></td><td class="name">Signal Flow</td><td>How well is energy flowing through these organs?</td><td>The 12 Signal Links together form a comprehensive communication network that directs the flow of energy and information around the body (instantaneously) ensuring that every bit of the body knows what it's doing and that information arrives.</td><td class="howto" rowspan="2">2. The Kelvaro scan reflects your energy interpretation at the moment of your scan, your energetic body may self correct, but it may not. In this case, running another scan in a week or so will help you interpret what specific actions are likely to give you the highest return.</td></tr>
      <tr><td></td><td class="name">Mind Body</td><td>How well is your mind body working?</td><td>The mind is the part of us that represents awareness and has two fundamental aspects: The part we rely on in our day to day activities and associated with thoughts, intellect, reasoning, beliefs, values, memories, conditional emotions.</td></tr>
      <tr><td></td><td class="name">Defence Zones</td><td>Where in your immune system need support?</td><td>The 16 Defence Zone fields form part of the human body-field and have many functions including: Providing healing messages for self repair of body tissues. Forming an important part of the body's 'energetic immune system'.</td><td class="howto" rowspan="2">3. If you choose to self direct your next steps, you will benefit from more than one scan. Kelvaro permits you to run a scan 1 x per 5 days.</td></tr>
      <tr><td></td><td class="name">Pathway Clusters</td><td>What combinations of bio-tonics look like resonating with your body?</td><td>The body provides itself with mini information networks which function as subsystems of the whole body-field and act as metabolic pathways governing energy usage. These subsystems are known as Pathway Clusters.</td></tr>
      <tr><td></td><td class="name">Block Points</td><td>Where is energy being blocked from flowing freely?</td><td>Where is energy blocked? The Block Points screen indicates specific anatomical points on the body where there are energetic blocks. The colour of the dots indicates the relative priority, with red/purple being the highest priority.</td><td class="howto" rowspan="2">4. If you chose to have your scan interpreted by a practitioner, a significant amount of time will be spent correlating how you feel with what shows up in the scan, which will lead to a much higher probability protocol, much earlier on.</td></tr>
      <tr><td></td><td class="name">Environment</td><td>What environmental toxins have left an energetic marker?</td><td>Damage to the body field by environmental factors can severely disrupt the functions of the Core Drivers and Signal Links and thus the regulation and functions of the physical body.</td></tr>
      <tr><td></td><td class="name">Nutrition</td><td>Nutrition: How well are you assimilating, absorbing and managing nutrients</td><td>Vitamins, minerals and other nutrients are fundamental requirements for the body to function. Optimum health requires that nutrients are managed correctly.</td><td class="howto" rowspan="2">5. Chose from 19 Bio-tonics from the Daily Balance Range</td></tr>
      <tr><td></td><td class="name">Recommendations</td><td>What recommendations would a practitioner discuss with you?</td><td>The Recommendation screen still reflects what a practitioner would be suggesting to you. However, as a Self Directed Account Holder, you may only purchase non prescription Kelvaro Health Bio-tonics.</td></tr>
    </tbody>
  </table>

  <div class="abs bottles" role="img" aria-label="Product photo: row of nineteen amber dropper bottles"></div>
  <div class="abs brand inside-brand"><span class="brand__dot"></span>VitalHaven.Studio</div>

  <div class="abs bio-panel"></div>
  <div class="abs portrait" role="img" aria-label="Portrait photo of the practitioner"></div>
  <h2 class="abs bio-name">Rowan T Hale</h2>
  <p class="abs bio-creds">FDN-P HPC PFC PBC</p>
  <div class="abs bio">
    <p>Rowan is a multimodality alternative health provider with a focus in shedding light on what holds you back from excellent functional health and showing up as the best version of yourself.</p>
    <p>He will set you up to run bioenergetic scanning at home and facilitate with you functional testing (as necessary), design supporting protocols and lifestyle frameworks to guide you on your path to wellness and beyond.</p>
    <p>It took Rowan almost 3 decades of trial and error, and false hope, for him to arrive at the same conclusion that leading experts in the field of bioenergetics had been saying since the beginning: energy drives biochemistry, not the other way round.</p>
    <p>This is foundational to how Kelvaro Health has become the leading provider of Bioenergetic scanning technology, and how it is helping to restore the energy and subsequent health of the world.</p>
    <p>Kelvaro has evolved over a 20 year period, 100s of 1000s of scans and now the ability for a client to operate the software from home, to either self direct, or operated it under the professional watch of Rowan and his team at vitalhaven.studio</p>
  </div>
  <blockquote class="abs bio-quote">In essence, Kelvaro gives you night goggles on what is going on for you, moreover what you can do about it. This is truly the future of medicine<cite>Rowan T Hale</cite></blockquote>

  <svg class="backdrop" width="1120" height="794" viewBox="0 0 1120 794" style="pointer-events:none">
    <defs>
      <linearGradient id="parkPhoto" x1="0" y1="0" x2="0" y2="1">
        <stop offset="0" stop-color="#b9d6e8"/><stop offset=".5" stop-color="#8fb06a"/><stop offset="1" stop-color="#5f8a3e"/>
      </linearGradient>
    </defs>
    <g role="img" aria-label="Photo: woman stretching her arms overhead in a sunny park">
      <path d="M790,794 C795,700 880,614 1010,604 C1060,600 1100,606 1120,612 L1120,794 Z" fill="url(#parkPhoto)"/>
    </g>
    <path d="M790,794 C795,700 880,614 1010,604 C1060,600 1100,606 1120,612" fill="none" stroke="#88d0c7" stroke-width="6"/>
  </svg>
</section>

</body>
</html>
```